Brightmoor Partners Branding Revamp

We are a consulting company, looking for a way to display and promote our brand. We have 2 sides to the business- Brightmoor (financial) and Partners (cyber security). The financial side products relate to business necessities: card processing, website design/hosting/maintenance, VoIP phone systems. The cyber security side promotes a bundled package of 4 solutions: network vulnerability scan, dark web scan, anti-ransomeware/malware software, and image-level backups. We want people to understand that partnering with Brightmoor Partners gives them “Elevated Peace of Mind” (tagline). Current badge and logos uploaded.

Target Market(s)

Small businesses

Contact Information for Business Card

Lena Marwick, Vice President, lena@brightmoorpartners.example, 555-806-1937, www.brightmoorpartners.example

Requirements
Nice to have
• I do prefer the darker background for front and back

```html
<!DOCTYPE html>
<html lang="en">
<head>
<meta charset="utf-8">
<title>Brightmoor Partners – Business Card</title>
<link href="https://fonts.googleapis.com/css2?family=Michroma&family=Exo+2:wght@400;500;600&display=swap" rel="stylesheet">
<style>
  :root {
    --backdrop: #1d1d22;
    --card-dark: #141416;
    --card-mid: #1f1f23;
    --red: #e3202a;
    --red-deep: #a5121a;
    --white: #f2f2f2;
    --grey: #d8d8d8;
  }
  * { box-sizing: border-box; margin: 0; padding: 0; }
  html, body { width: 1200px; height: 800px; overflow: hidden; }
  body {
    background: var(--backdrop);
    position: relative;
    font-family: "Exo 2", sans-serif;
    color: var(--white);
  }
  .card {
    position: absolute;
    top: 245px;
    width: 540px;
    height: 310px;
    border-radius: 22px;
    background: linear-gradient(135deg, var(--card-mid), var(--card-dark));
    overflow: hidden;
    box-shadow: 0 18px 40px rgba(0,0,0,.45);
  }
  .card--front { left: 50px; }
  .card--back { left: 610px; }

  /* front */
  .front-brand {
    position: absolute;
    top: 92px;
    left: 0; right: 0;
    text-align: center;
  }
  .front-wordmark {
    font-family: "Michroma", sans-serif;
    font-size: 24px;
    letter-spacing: 5px;
    color: var(--white);
    line-height: 1.5;
  }
  .front-tagline {
    margin-top: 10px;
    font-family: "Michroma", sans-serif;
    font-size: 9px;
    letter-spacing: 3px;
    color: var(--red);
    text-transform: uppercase;
  }
  .front-band {
    position: absolute;
    left: 0; right: 0;
    top: 236px;
    height: 30px;
    background: linear-gradient(90deg, var(--red-deep), var(--red) 40%, var(--red-deep));
    display: flex;
    align-items: center;
    justify-content: center;
    font-family: "Michroma", sans-serif;
    font-size: 10px;
    letter-spacing: 3px;
    color: var(--white);
    text-transform: uppercase;
  }

  /* back */
  .back-band {
    position: absolute;
    top: 0; right: 0;
    width: 200px;
    height: 100%;
    background: linear-gradient(160deg, var(--red), var(--red-deep) 70%, #5e0a0f);
  }
  .back-content {
    position: absolute;
    left: 36px;
    top: 44px;
    width: 290px;
  }
  .back-wordmark {
    font-family: "Michroma", sans-serif;
    font-size: 19px;
    letter-spacing: 4px;
    color: var(--white);
    line-height: 1.45;
  }
  .person { margin-top: 26px; }
  .person-name {
    font-family: "Michroma", sans-serif;
    font-size: 15px;
    letter-spacing: 2px;
    text-transform: uppercase;
  }
  .person-role {
    font-family: "Michroma", sans-serif;
    font-size: 9px;
    letter-spacing: 2px;
    color: var(--red);
    text-transform: uppercase;
    margin-top: 4px;
  }
  .contact-list { list-style: none; margin-top: 16px; }
  .contact-item {
    display: flex;
    align-items: flex-start;
    gap: 10px;
    font-size: 12.5px;
    color: var(--grey);
    line-height: 1.35;
    margin-bottom: 5px;
    white-space: nowrap;
  }
  .contact-icon { width: 15px; height: 15px; flex: none; margin-top: 1px; }
</style>
</head>
<body>

  <section class="card card--front" aria-label="Card front">
    <div class="front-brand">
      <div class="front-wordmark">BRIGHTMOOR<br>PARTNERS</div>
      <div class="front-tagline">Elevated Peace of Mind</div>
    </div>
    <div class="front-band">www.brightmoorpartners.example</div>
  </section>

  <section class="card card--back" aria-label="Card back">
    <div class="back-band" role="img" aria-label="Red decorative panel"></div>
    <div class="back-content">
      <div class="back-wordmark">BRIGHTMOOR<br>PARTNERS</div>
      <div class="person">
        <div class="person-name">Lena Marwick</div>
        <div class="person-role">Vice President</div>
      </div>
      <ul class="contact-list">
        <li class="contact-item">
          <svg class="contact-icon" viewBox="0 0 16 16"><circle cx="8" cy="8" r="8" fill="#e3202a"/><path d="M5 4.5l1.5-.5 1 2-1 .8c.4 1 1.2 1.8 2.2 2.2l.8-1 2 1-.5 1.5c-3 .2-6.2-3-6-6z" fill="#fff"/></svg>
          555-806-1937
        </li>
        <li class="contact-item">
          <svg class="contact-icon" viewBox="0 0 16 16"><circle cx="8" cy="8" r="8" fill="#e3202a"/><rect x="4" y="5" width="8" height="6" fill="none" stroke="#fff" stroke-width="1.1"/><path d="M4 5l4 3.2L12 5" fill="none" stroke="#fff" stroke-width="1.1"/></svg>
          lena@brightmoorpartners.example
        </li>
        <li class="contact-item">
          <svg class="contact-icon" viewBox="0 0 16 16"><circle cx="8" cy="8" r="8" fill="#e3202a"/><circle cx="8" cy="8" r="4" fill="none" stroke="#fff" stroke-width="1"/><path d="M4 8h8M8 4c-1.6 2.4-1.6 5.6 0 8M8 4c1.6 2.4 1.6 5.6 0 8" fill="none" stroke="#fff" stroke-width="1"/></svg>
          www.brightmoorpartners.example
        </li>
        <li class="contact-item">
          <svg class="contact-icon" viewBox="0 0 16 16"><circle cx="8" cy="8" r="8" fill="#e3202a"/><path d="M8 12.5s-3-3.2-3-5.3a3 3 0 016 0c0 2.1-3 5.3-3 5.3z" fill="#fff"/><circle cx="8" cy="7.2" r="1.1" fill="#e3202a"/></svg>
          <span>48 Harlow Street NW<br>Suite 400, Elmfield<br>MI 00000</span>
        </li>
      </ul>
    </div>
  </section>

</body>
</html>
```